Website design for a Recruitment Agency in the Pacific Islands

Website for jobseekers to search for work, employers to list vacancies and also for workers to upload their resumes for possible job prospects.

The website will be called ' Korvani Staffing' and this needs to reflect the Pacific Islanders searching for jobs or working in the fields.
Must be connected to a database that collects details for workers which can be downloaded onto an excel spreadsheet for quick reviews offline
The website must also have an app for ios and android so this can be easily downloaded for individuals who want to do quick job searches without going onto the website.

The main objective of this website is to list job opportunities in all Pacific Island Countries or even overseas which Pacific Islanders can apply.

The theme of fishing means ' there is alot of fish in the sea ' = lots of workers in the Pacific Ocean.

Target Market(s)

Agriculture, Fisheries, constructions and mining

Industry/Entity Type

Agriculture, Constructions and Fisheries

Font styles to use
Other font styles liked:
• Muli

Colors
E54698
E96AAD
F1A4CE
F9D9EA
FCEFF6

Requirements
Must have
• Must have an App, adroid and ios
Nice to have
• - pictures of Pacific Islanders , pictures of Pacific Islanders at work in mines, in fisheries and in agricultures

```html
<!DOCTYPE html>
<html lang="en">
<head>
<meta charset="utf-8">
<title>Korvani Staffing — Recruitment Agency in the Pacific Islands</title>
<link rel="stylesheet" href="https://fonts.googleapis.com/css2?family=Mulish:ital,wght@0,300;0,400;0,600;1,400&display=swap">
<style>
:root{
  --pink:#E54698;
  --pink-2:#E96AAD;
  --pink-3:#F1A4CE;
  --pink-4:#F9D9EA;
  --pink-5:#FCEFF6;
  --ink:#222;
  --body:#555;
  --grey-bg:#f5f5f5;
  --footer:#1b1b1d;
  --white:#fff;
}
*{box-sizing:border-box;margin:0;padding:0}
html,body{width:1200px;height:4148px;overflow:hidden}
body{font-family:"Mulish",sans-serif;color:var(--ink);background:var(--white);position:relative}
section,header,footer{position:absolute;left:0;width:1200px}
.btn-outline{position:absolute;display:flex;align-items:center;justify-content:center;border:2px solid currentColor;border-radius:30px;font-size:18px;letter-spacing:.5px;text-transform:uppercase}

/* header */
.site-header{top:0;height:112px;background:var(--white);z-index:3}
.logo-box{position:absolute;left:111px;top:0;width:160px;height:193px;background:var(--pink);padding:18px 20px;color:var(--white);font-weight:300;font-size:17px;line-height:1}
.logo-box span{display:block}
.logo-box span+span{padding-left:24px}
.logo-box .mark-dot{width:12px;height:12px;border-radius:50%;background:var(--white);margin-top:14px}
.util-nav{position:absolute;right:112px;top:22px;display:flex;gap:12px;font-size:16px;align-items:center}
.util-nav .search{font-size:14px;color:#777;margin-right:22px}
.util-nav .acct{color:var(--ink)}
.util-nav .acct b{color:var(--pink);font-weight:400}
.main-nav{position:absolute;right:112px;top:66px;display:flex;gap:20px;font-size:17px}
.main-nav .active{color:var(--pink)}

/* hero */
.hero{top:112px;height:628px;background:linear-gradient(100deg,#4a5a3a 0%,#6d7d52 35%,#8e8a6c 60%,#3d4d6a 100%)}
.hero .photo{position:absolute;inset:0}
.hero h1{position:absolute;left:108px;top:160px;font-size:60px;font-weight:300;color:var(--white)}
.hero .tagline{position:absolute;left:113px;top:250px;font-size:18px;color:var(--white)}
.hero .btn-outline{left:111px;top:303px;width:204px;height:66px;color:var(--white)}
.hero .downloads{position:absolute;left:111px;top:393px;font-size:21px;font-style:italic;color:var(--white)}
.store-row{position:absolute;display:flex;gap:12px}
.store-btn{width:168px;height:48px;background:#000;border:1px solid #888;border-radius:7px;color:var(--white);display:flex;flex-direction:column;justify-content:center;padding-left:40px;position:relative}
.store-btn::before{content:"";position:absolute;left:13px;top:15px;width:17px;height:17px;border-radius:50%;background:var(--white)}
.store-btn small{font-size:9px;text-transform:uppercase}
.store-btn strong{font-size:18px;font-weight:600;line-height:1.1}
.hero .store-row{left:111px;top:442px}
.hero .slider-dots{position:absolute;left:566px;top:566px;display:flex;gap:6px}
.slider-dots i{width:18px;height:4px;background:var(--white)}
.slider-dots i.on{background:var(--pink)}

/* split */
.split{top:740px;height:312px;display:flex}
.split .half{width:600px;height:312px;position:relative;padding:32px 0 0 110px}
.split .employer{background:#f6f6f6}
.split .seeker{background:var(--pink);color:var(--white);padding-left:37px}
.split .kicker{font-size:21px;font-style:italic;color:var(--pink)}
.split .seeker .kicker{color:var(--white)}
.split h2{font-size:38px;font-weight:400;margin:2px 0 22px}
.split p{font-size:16px;line-height:26px;width:440px;color:var(--body)}
.split .seeker p{color:var(--white)}
.split .btn-outline{top:198px;width:153px;height:58px;color:var(--pink)}
.split .employer .btn-outline{left:110px}
.split .seeker .btn-outline{left:37px;width:212px;color:var(--white)}

/* welcome */
.welcome{top:1052px;height:548px}
.welcome .ph{position:absolute}
.ph-one{left:111px;top:66px;width:222px;height:343px;background:linear-gradient(180deg,#c9d5e3,#7b8aa0 60%,#3f5266)}
.ph-two{left:351px;top:131px;width:221px;height:342px;background:linear-gradient(180deg,#efe9e4,#cfc6bf 60%,#8d7d76)}
.welcome h2{position:absolute;left:639px;top:54px;font-size:40px;font-weight:400;line-height:46px}
.welcome p{position:absolute;left:641px;top:172px;width:440px;font-size:16px;line-height:25.8px;color:var(--body)}
.welcome .btn-outline{left:641px;top:408px;width:161px;height:58px;color:var(--pink)}

/* services */
.services{top:1600px;height:435px;background:var(--grey-bg)}
.services h2{position:absolute;width:100%;top:46px;text-align:center;font-size:40px;font-weight:400}
.svc-list{position:absolute;left:0;top:137px;width:100%}
.svc{position:absolute;width:220px;margin-left:-110px;text-align:center}
.svc .circle{width:160px;height:160px;border-radius:50%;background:var(--white);margin:0 auto;display:flex;align-items:center;justify-content:center}
.svc.on .circle{background:var(--pink)}
.svc .label{margin-top:18px;font-size:22px;line-height:26px}

/* jobs */
.jobs{top:2035px;height:858px}
.jobs h2{position:absolute;width:100%;top:56px;text-align:center;font-size:40px;font-weight:400}
.job-table{position:absolute;left:111px;top:158px;width:977px}
.job-head,.job-row{display:flex;align-items:center}
.job-head{height:42px;font-size:19px}
.job-row{height:128px}
.job-row.tint{background:var(--pink-5)}
.col-title{width:616px;padding-left:22px;display:flex;align-items:center;gap:12px}
.job-head .col-title{justify-content:center;padding-left:0;width:540px}
.col-type{width:180px;text-align:center;font-size:16px;color:var(--body)}
.job-head .col-type,.job-head .col-loc{color:var(--ink);font-size:19px}
.job-head .col-type{width:160px}
.col-loc{width:200px;text-align:center;font-size:16px;color:var(--body)}
.job-row .col-loc{margin-top:-10px}
.job-row .col-type{margin-top:12px}
.co-badge{width:72px;height:72px;border-radius:50%;background:#e4e4e4;flex:none}
.job-name{font-size:20px;line-height:28px}
.job-org{font-size:16px;color:var(--body)}
.pin{color:var(--pink)}
.jobs .btn-outline{left:520px;top:733px;width:161px;height:57px;color:var(--pink)}

/* join */
.join{top:2893px;height:540px;background:var(--pink);overflow:hidden}
.join h2{position:absolute;left:110px;top:112px;font-size:40px;font-weight:400;line-height:46px;color:var(--white)}
.join p{position:absolute;left:111px;top:226px;width:480px;font-size:16px;line-height:27px;color:var(--white)}
.join .btn-outline{left:111px;top:363px;width:189px;height:57px;color:var(--white)}
.join .ph-circle{position:absolute;left:630px;top:68px;width:470px;height:470px;border-radius:50%;background:radial-gradient(circle at 50% 45%,#d9b59c,#9b6f58 55%,#5c4538);border:4px solid var(--white)}

/* app */
.app{top:3433px;height:278px;text-align:center}
.app h2{position:absolute;width:100%;top:54px;font-size:40px;font-weight:400}
.app .sub{position:absolute;width:100%;top:112px;font-size:16px;color:var(--body)}
.app .store-row{left:429px;top:162px}

/* footer */
.site-footer{top:3711px;height:437px;background:var(--footer);color:var(--white)}
.foot-logo{position:absolute;left:111px;top:30px;width:220px;height:250px}
.foot-logo .name{font-size:26px;font-weight:300;line-height:26px}
.foot-logo .name span{display:block;padding-left:36px}
.foot-logo .dot{width:12px;height:12px;border-radius:50%;background:var(--white);margin:16px 0 0 50px}
.foot-col{position:absolute;top:52px}
.foot-col h3{font-size:19px;font-weight:400;margin-bottom:20px}
.foot-col li{list-style:none;font-size:16px;line-height:26px}
.foot-col.quick{left:414px}
.foot-col.train{left:577px}
.partner{position:absolute;left:865px;top:60px;width:222px;display:flex;flex-direction:column;align-items:center;gap:18px}
.partner .badge{width:120px;height:100px;border-radius:8px;background:#3a3a3d}
.partner .pname{font-size:19px;font-weight:600}
.foot-rule{position:absolute;left:111px;top:335px;width:977px;height:1px;background:#555}
.copyright{position:absolute;left:111px;top:378px;font-size:16px}
.social{position:absolute;right:112px;top:366px;display:flex;gap:12px}
.social i{width:40px;height:40px;border-radius:50%;border:1.5px solid var(--white)}
</style>
</head>
<body>

<header class="site-header">
  <div class="logo-box">
    <span>korvani</span><span>staffing</span>
    <div class="mark-dot"></div>
  </div>
  <div class="util-nav">
    <span class="search">&#9906; Job Search</span>
    <span class="acct"><b>&#9632;</b> Login</span><span>|</span><span class="acct"><b>&#9679;</b> Join</span>
  </div>
  <nav class="main-nav">
    <a class="active">Home</a><a>Abous Us</a><a>Services</a><a>Job Seeker</a><a>Training</a><a>Resources</a><a>Contact Us</a>
  </nav>
</header>

<section class="hero">
  <div class="photo" role="img" aria-label="Pacific Islander woman in a cap smiling while tending green plants in a nursery"></div>
  <h1>Korvani Staffing</h1>
  <p class="tagline">We are a Recruitment Agency in the Pacific Islands</p>
  <a class="btn-outline">Get More Info</a>
  <p class="downloads">#1 most downloaded app</p>
  <div class="store-row">
    <a class="store-btn"><small>Get it on</small><strong>Droid Market</strong></a>
    <a class="store-btn"><small>Download on the</small><strong>Phone Shop</strong></a>
  </div>
  <div class="slider-dots"><i></i><i class="on"></i><i></i></div>
</section>

<section class="split">
  <div class="half employer">
    <p class="kicker">List Vacancies</p>
    <h2>Employer</h2>
    <p>Nemo enim ipsam voluptatem quia voluptas sit aspern atur aut odit aut fugitd quia cons.</p>
    <a class="btn-outline">Post Jobs</a>
  </div>
  <div class="half seeker">
    <p class="kicker">Find a Job</p>
    <h2>Job Seeker</h2>
    <p>Nemo enim ipsam voluptatem quia voluptas sit aspern atur aut odit aut fugitd quia cons.</p>
    <a class="btn-outline">Upload Resume</a>
  </div>
</section>

<section class="welcome">
  <div class="ph ph-one" role="img" aria-label="Fisherman in gloves and apron hauling a line by the sea"></div>
  <div class="ph ph-two" role="img" aria-label="Young woman working on a laptop at home"></div>
  <h2>Welcome to<br>Korvani Staffing</h2>
  <p>Korvani Staffing PTY LTD is a labour hire recruiting and logistical support service located, in both Papua New Guinea and Australia. With its headquarters located in Newcastle NSW Australia, while also having an office base in Port Moresby Papua New Guinea run by Tomas and his team with Reefline Logistics. Our aim is to assist in supporting with various requirements needed to be met by the Pacific TIDE scheme in Australia...</p>
  <a class="btn-outline">View More</a>
</section>

<section class="services">
  <h2>Services we offer assistance in</h2>
  <div class="svc-list">
    <div class="svc" style="left:208px">
      <div class="circle"><svg width="76" height="76" viewBox="0 0 76 76" fill="none" stroke="#E54698" stroke-width="2.5"><circle cx="38" cy="30" r="6"/><path d="M28 50v-8a10 10 0 0 1 20 0v8"/><circle cx="14" cy="12" r="5"/><circle cx="62" cy="12" r="5"/><circle cx="14" cy="58" r="5"/><circle cx="62" cy="58" r="5"/><path d="M6 34h16M54 34h16M10 30l-4 4 4 4M66 30l4 4-4 4"/></svg></div>
      <p class="label">Recruitment<br>process outsourced</p>
    </div>
    <div class="svc" style="left:416px">
      <div class="circle"><svg width="80" height="76" viewBox="0 0 80 76" fill="none" stroke="#E54698" stroke-width="2.5"><rect x="6" y="16" width="50" height="40" rx="4"/><path d="M22 16V8h18v8M12 28h30M12 36h22M12 44h18"/><circle cx="58" cy="52" r="16"/><path d="M58 42v10l6 4"/></svg></div>
      <p class="label">Temporary<br>hire</p>
    </div>
    <div class="svc on" style="left:609px">
      <div class="circle"><svg width="80" height="76" viewBox="0 0 80 76" fill="none" stroke="#fff" stroke-width="2.5"><circle cx="32" cy="20" r="12"/><path d="M10 60v-8a16 16 0 0 1 32 0"/><rect x="40" y="42" width="34" height="26" rx="3"/><path d="M50 42v-5h14v5M50 56l5 5 10-10"/></svg></div>
      <p class="label">Permanent<br>hire</p>
    </div>
    <div class="svc" style="left:801px">
      <div class="circle"><svg width="76" height="76" viewBox="0 0 76 76" fill="none" stroke="#E54698" stroke-width="2.5"><circle cx="38" cy="34" r="20"/><circle cx="38" cy="34" r="11"/><path d="M38 8v6M38 54v6M12 34h6M58 34h6M20 16l4 4M52 48l4 4M56 16l-4 4M20 52l4-4M22 70l16-14 16 14"/></svg></div>
      <p class="label">Managed<br>services</p>
    </div>
    <div class="svc" style="left:994px">
      <div class="circle"><svg width="76" height="76" viewBox="0 0 76 76" fill="none" stroke="#E54698" stroke-width="2.5"><circle cx="38" cy="26" r="10"/><path d="M38 20v6l4 3M30 58v-8a8 8 0 0 1 16 0v8z"/><circle cx="38" cy="44" r="4"/><path d="M8 8l12 12M68 8L56 20M8 50l12-8M68 50l-12-8M8 8h8M8 8v8M68 8h-8M68 8v8"/></svg></div>
      <p class="label">Tides</p>
    </div>
  </div>
</section>

<section class="jobs">
  <h2>Latest job listings</h2>
  <div class="job-table">
    <div class="job-head"><div class="col-title">Job title</div><div class="col-type">Job type</div><div class="col-loc">Location</div></div>
    <div class="job-row tint"><div class="col-title"><span class="co-badge"></span><div><div class="job-name">Community Development Specialist</div><div class="job-org">Coral Reach Partnerships Program - Tidewell Global</div></div></div><div class="col-type">Full Time</div><div class="col-loc"><span class="pin">&#9679;</span> Papua New Guinea</div></div>
    <div class="job-row"><div class="col-title"><span class="co-badge"></span><div><div class="job-name">Community Development Specialist</div><div class="job-org">Coral Reach Partnerships Program - Tidewell Global</div></div></div><div class="col-type">Full Time</div><div class="col-loc"><span class="pin">&#9679;</span> Papua New Guinea</div></div>
    <div class="job-row tint"><div class="col-title"><span class="co-badge"></span><div><div class="job-name">Community Development Specialist</div><div class="job-org">Coral Reach Partnerships Program - Tidewell Global</div></div></div><div class="col-type">Full Time</div><div class="col-loc"><span class="pin">&#9679;</span> Papua New Guinea</div></div>
    <div class="job-row"><div class="col-title"><span class="co-badge"></span><div><div class="job-name">Community Development Specialist</div><div class="job-org">Coral Reach Partnerships Program - Tidewell Global</div></div></div><div class="col-type">Full Time</div><div class="col-loc"><span class="pin">&#9679;</span> Papua New Guinea</div></div>
  </div>
  <a class="btn-outline">View More</a>
</section>

<section class="join">
  <h2>Want to join the TIDE<br>scheme?</h2>
  <p>Nemo enim ipsam voluptatem quia voluptas sit aspernatur aut odit aut fugit, sed quia consequuntur magni dolores eos qui ratione volu ptatem sequi nesciunt.Neque porro quisquam est, qui dolorem ipsum quia dolor sit amet, consectetu.</p>
  <a class="btn-outline">Join Us Now</a>
  <div class="ph-circle" role="img" aria-label="Pacific Islander mother and daughter smiling together"></div>
</section>

<section class="app">
  <h2>Download our app</h2>
  <p class="sub">Any time, anywhere. Whenever you want</p>
  <div class="store-row">
    <a class="store-btn"><small>Get it on</small><strong>Droid Market</strong></a>
    <a class="store-btn"><small>Download on the</small><strong>Phone Shop</strong></a>
  </div>
</section>

<footer class="site-footer">
  <div class="foot-logo">
    <div class="name">korvani<span>staffing</span></div>
    <div class="dot"></div>
  </div>
  <div class="foot-col quick">
    <h3>Quick Links</h3>
    <ul><li>Home</li><li>Abous Us</li><li>Services</li><li>Job Seeker</li><li>Training</li><li>Resources</li><li>Contact Us</li></ul>
  </div>
  <div class="foot-col train">
    <h3>Training</h3>
    <ul><li>First Aid</li><li>Health And Hygene</li><li>Manual Handeling</li><li>Workplace Health And Safety</li></ul>
  </div>
  <div class="partner">
    <div class="badge"></div>
    <div class="pname">Partner Government</div>
  </div>
  <div class="foot-rule"></div>
  <p class="copyright">2022 &copy; Copyright, Korvani Staffing. All rights reserved.</p>
  <div class="social"><i></i><i></i><i></i></div>
</footer>

</body>
</html>
```